Vantage Forge needs a powerpoint design

We need a powerpoint design for an Information Technology based in Fairfax call "Vantage Forge". We are Information Technology solutions provider for the Federal Government. We develop Kestrel, Mobile and Cloud based solutions. We support the Healthcare and Financial sectors of the Government. We would like to see designs that use the colors of our logo. We've attached a copy of our logo. The final design should communicate Information Technology and System Integration with Agile Development.

Target Market(s)

Our target market is the Federal Government and System Integators in the Washington DC area.

Industry/Entity Type

Government

Requirements
Must have
• The powerpoint design must have a professional look.

```html
<!DOCTYPE html>
<html lang="en">
<head>
<meta charset="utf-8">
<title>Vantage Forge – Presentation Templates</title>
<link href="https://fonts.googleapis.com/css2?family=Montserrat:wght@600;800&display=swap" rel="stylesheet">
<style>
  :root {
    --steel-light: #e4e6e9;
    --steel-mid: #c3c6cb;
    --steel-dark: #9a9ea4;
    --brand-blue: #233f8f;
    --brand-icon: #2c4f9e;
    --sky-teal: #1aa6a8;
    --sky-amber: #f2a64a;
    --city-dark: #2a2a2c;
    --night-blue: #1f3f8c;
    --seal-copper: #c47a4e;
    --guide-teal: #5cb3b0;
  }
  * { box-sizing: border-box; margin: 0; padding: 0; }
  html, body { width: 1200px; height: 900px; overflow: hidden; }
  body {
    position: relative;
    font-family: "Montserrat", Arial, sans-serif;
    background:
      repeating-linear-gradient(160deg, rgba(255,255,255,.18) 0 1px, rgba(0,0,0,.04) 1px 3px),
      linear-gradient(135deg, var(--steel-mid), var(--steel-light) 45%, var(--steel-dark) 100%);
  }
  .slide {
    position: absolute;
    overflow: hidden;
    background:
      repeating-linear-gradient(160deg, rgba(255,255,255,.22) 0 1px, rgba(0,0,0,.05) 1px 3px),
      linear-gradient(120deg, var(--steel-dark), var(--steel-light) 40%, var(--steel-mid) 70%, var(--steel-light));
    box-shadow: 0 0 0 1px rgba(0,0,0,.25), 2px 3px 6px rgba(0,0,0,.35), inset 1px 1px 0 rgba(255,255,255,.7);
  }
  .slide--title   { left: 0;   top: 0;   width: 551px; height: 412px; }
  .slide--section { left: 639px; top: 6px; width: 547px; height: 412px; }
  .slide--content { left: 12px;  top: 436px; width: 550px; height: 410px; }
  .slide--gallery { left: 639px; top: 436px; width: 547px; height: 410px; }

  .brand { position: absolute; left: 12px; top: 10px; display: flex; align-items: flex-start; gap: 12px; }
  .brand__mark { width: 30px; height: 30px; background: var(--brand-icon); margin-top: 2px; }
  .brand__name { font-weight: 800; font-size: 22px; color: var(--brand-blue); letter-spacing: .2px; line-height: 1; text-transform: uppercase; white-space: nowrap; }
  .brand__tagline { font-weight: 600; font-size: 7px; color: var(--brand-blue); letter-spacing: .2px; margin-top: 4px; text-transform: uppercase; white-space: nowrap; }

  .scene { position: absolute; inset: 0; width: 100%; height: 100%; }

  .guide { position: absolute; top: 0; bottom: 0; width: 1px; background: var(--guide-teal); opacity: .8; }

  .content-panel {
    position: absolute; left: 8px; top: 6px; width: 396px; height: 392px;
    background: rgba(255,255,255,.12);
    box-shadow: inset 0 0 0 1px rgba(255,255,255,.3);
  }
  .thumb {
    position: absolute; left: 418px; width: 108px; height: 108px; border-radius: 14px;
    border: 2px solid rgba(255,255,255,.8);
    box-shadow: 1px 2px 4px rgba(0,0,0,.35);
  }
  .thumb--city  { top: 20px;  background: linear-gradient(180deg, var(--sky-teal), var(--sky-amber) 45%, var(--city-dark) 70%); }
  .thumb--seal  { top: 150px; background: radial-gradient(circle at 50% 50%, var(--seal-copper) 0 38%, #d9d9d9 39%, #a8a8a8 100%); }
  .thumb--river { top: 280px; background: linear-gradient(180deg, var(--night-blue), #2c5ab5 45%, #e0894a 55%, #3a2f6e 75%, #1b1f4a); }
</style>
</head>
<body>

  <section class="slide slide--title">
    <svg class="scene" viewBox="0 0 551 412" role="img" aria-label="Photo of a city skyline at dusk with lit streets">
      <defs>
        <linearGradient id="dusk" x1="0" y1="0" x2="0" y2="1">
          <stop offset="0" stop-color="#1aa6a8"/>
          <stop offset=".35" stop-color="#f2a64a"/>
          <stop offset=".55" stop-color="#5a4a3a"/>
          <stop offset="1" stop-color="#1f2a22"/>
        </linearGradient>
      </defs>
      <path d="M551,90 C390,108 252,240 228,412 L551,412 Z" fill="url(#dusk)"/>
    </svg>
    <div class="brand">
      <div class="brand__mark"></div>
      <div><div class="brand__name">Vantage Forge</div><div class="brand__tagline">Turning bold ideas into working systems</div></div>
    </div>
  </section>

  <section class="slide slide--section">
    <span class="guide" style="left:136px"></span>
    <span class="guide" style="left:274px"></span>
    <svg class="scene" viewBox="0 0 547 412" role="img" aria-label="Photo band of a city tower at dusk">
      <defs>
        <linearGradient id="dusk2" x1="0" y1="0" x2="0" y2="1">
          <stop offset="0" stop-color="#1aa6a8"/>
          <stop offset=".25" stop-color="#f2a64a"/>
          <stop offset=".5" stop-color="#4d4436"/>
          <stop offset="1" stop-color="#1f2a22"/>
        </linearGradient>
      </defs>
      <path d="M334,0 C296,120 286,260 316,412 L451,412 C418,280 410,130 457,0 Z" fill="url(#dusk2)"/>
    </svg>
    <div class="brand">
      <div class="brand__mark"></div>
      <div><div class="brand__name">Vantage Forge</div><div class="brand__tagline">Turning bold ideas into working systems</div></div>
    </div>
  </section>

  <section class="slide slide--content">
    <div class="brand">
      <div class="brand__mark"></div>
      <div><div class="brand__name">Vantage Forge</div><div class="brand__tagline">Turning bold ideas into working systems</div></div>
    </div>
  </section>

  <section class="slide slide--gallery">
    <div class="content-panel"></div>
    <div class="brand">
      <div class="brand__mark"></div>
      <div><div class="brand__name">Vantage Forge</div><div class="brand__tagline">Turning bold ideas into working systems</div></div>
    </div>
    <div class="thumb thumb--city" role="img" aria-label="City skyline at dusk"></div>
    <div class="thumb thumb--seal" role="img" aria-label="Round county seal plaque"></div>
    <div class="thumb thumb--river" role="img" aria-label="Waterfront city lights at night"></div>
  </section>

</body>
</html>
```